Economic Development Consulting needs killer brochure for Northfield Civic Design Union Conference

Bramblecrest Partners is an elite sponsor for the NCDU conference this year. Our Three service offerings for the event are
Economic Development Master Planning (and our proprietary approach)
Feasibility Studies and Site Options Analysis (also leverages our proprietary approach)
Resilience Assessment & Planning
Our slogan is Customized consulting for communities and community planners and Uncommon Insights — Aligning Resources to Opportunity

We need a square, trifold brochure, and we would like 3 posters, one dedicated to each of our service offerings, matching the brochure.

The NCDU conference site is http://www.ncdumeridian.example/yearly-summit
Updates

We have increased the budget for the brochure requested. The posters referenced int eh posting will be a separate project, offered to the designer who designs the brochure.

Project Deadline Extended
Reason: We are looking at adding some additional text.

Target Market(s)

Planners, Architects,

Industry/Entity Type

Consulting

Font styles to use
Sans Serif

Colors
0255a3

Requirements
Must have
• Square, trifold

```html
<!DOCTYPE html>
<html lang="en">
<head>
<meta charset="utf-8">
<title>Bramblecrest Partners – Square Trifold Brochure</title>
<link rel="stylesheet" href="https://fonts.googleapis.com/css2?family=Exo+2:wght@300;400;600&family=Open+Sans:wght@400;600;700&display=swap">
<style>
  :root{
    --canvas:#dcdcdc;
    --paper:#0b0b0c;
    --heading:#6fe3c6;
    --accent:#1fb6e8;
    --brand-blue:#0255a3;
    --tile:#145e6b;
    --tile-icon:#6fb9c4;
    --rule:#2bb3a6;
    --text:#f2f2f2;
    --muted:#8a8f93;
    --overlay:rgba(22,110,124,.92);
    --photo-a:#9aa1a6;
    --photo-b:#d7d9da;
  }
  *{box-sizing:border-box;margin:0;padding:0}
  html,body{width:1200px;height:800px;overflow:hidden}
  body{background:var(--canvas);font-family:"Open Sans",Arial,sans-serif;color:var(--text)}
  .brochure{position:absolute;left:15px;top:205px;width:1170px;height:390px;display:flex;box-shadow:0 14px 30px rgba(0,0,0,.25)}
  .panel{position:relative;width:390px;height:390px;background:var(--paper);overflow:hidden}
  .panel + .panel{border-left:1px solid #1c1c1e}
  .accent-bar{position:absolute;left:24px;top:26px;width:26px;height:4px;background:var(--accent)}
  .panel-title{font-family:"Exo 2",Arial,sans-serif;font-weight:300;color:var(--heading);font-size:28px;line-height:1.08;letter-spacing:.2px}
  .bullets{list-style:none;font-family:"Exo 2",Arial,sans-serif;font-size:11px;line-height:1.4;color:var(--text)}
  .bullets li::before{content:"• "}
  .fine{font-size:5.6px;line-height:1.5;color:var(--muted)}
  .fine strong{color:var(--text);font-weight:600}
  .rule{position:absolute;height:2px;background:var(--rule)}

  /* Left panel */
  .feasibility .panel-title{position:absolute;left:24px;top:38px;width:345px}
  .feasibility .bullets{position:absolute;left:24px;top:112px}
  .features{position:absolute;left:24px;top:170px;display:flex;gap:8px}
  .feature{width:62px}
  .feature-tile{width:62px;height:58px;background:var(--tile);display:flex;align-items:center;justify-content:center}
  .feature-tile svg{width:20px;height:20px;fill:none;stroke:var(--tile-icon);stroke-width:1.5}
  .feature-label{font-size:6.5px;color:var(--text);margin:5px 0 4px;white-space:nowrap}
  .company{position:absolute;left:24px;top:322px;display:flex;gap:22px}
  .company-label{font-size:6.5px;font-weight:700;color:var(--rule);letter-spacing:.4px;margin-bottom:2px}
  .feasibility .rule{left:24px;top:306px;width:342px}

  /* Middle panel */
  .team .panel-title{position:absolute;left:24px;top:24px;width:120px;font-size:25px}
  .photo{position:absolute;background:linear-gradient(160deg,var(--photo-b),var(--photo-a))}
  .photo-tag{position:absolute;top:4px;right:4px;width:9px;height:9px;background:var(--accent);font-size:5px;line-height:9px;text-align:center;color:#0b0b0c}
  .photo-strip{position:absolute;bottom:0;right:0;width:30px;height:3px;background:var(--accent)}
  .team-lead{position:absolute;left:24px;top:208px;width:342px;font-size:7.4px;font-weight:600;line-height:1.4}
  .team-columns{position:absolute;left:24px;top:238px;width:342px;display:flex;gap:12px}
  .team-columns > div{flex:1}
  .team-columns p + p{margin-top:5px}
  .team .rule{left:24px;top:332px;width:342px}

  /* Right panel */
  .resilience .panel-title{position:absolute;left:24px;top:38px;width:300px}
  .resilience .bullets{position:absolute;left:24px;top:104px}
  .resilience-copy{position:absolute;left:24px;top:160px;width:118px}
  .resilience-copy p + p{margin-top:5px}
  .resilience .rule{left:24px;top:344px;width:110px}
  .hero-photo{left:150px;top:166px;width:240px;height:224px;background:linear-gradient(135deg,#eef1f2 0%,#c9cfd2 50%,#8d969b 80%,var(--brand-blue) 100%)}
  .overlay{position:absolute;left:150px;top:290px;width:210px;padding:7px 9px;background:var(--overlay);font-size:7px;font-weight:600;line-height:1.35;color:#fff}
</style>
</head>
<body>
<main class="brochure">

  <section class="panel feasibility">
    <span class="accent-bar"></span>
    <h2 class="panel-title">Feasibility Studies and Site Options Analysis</h2>
    <ul class="bullets">
      <li>Comprehensive analysis of current state and options</li>
      <li>Statisticalmodeling tool creates best fit scenarios</li>
      <li>Strategic planning for current and future use</li>
    </ul>
    <div class="features">
      <div class="feature">
        <div class="feature-tile"><svg viewBox="0 0 20 20"><path d="M5 2h7l4 4v12H5z"/><path d="M12 2v4h4"/></svg></div>
        <p class="feature-label">Well documented</p>
        <p class="fine">Our proprietary approach documents every finding with clear sources.</p>
      </div>
      <div class="feature">
        <div class="feature-tile"><svg viewBox="0 0 20 20"><path d="M10 2l7 3v5c0 4-3 7-7 8-4-1-7-4-7-8V5z"/></svg></div>
        <p class="feature-label">Maximum Security</p>
        <p class="fine">Sensitive community data stays protected at each stage.</p>
      </div>
      <div class="feature">
        <div class="feature-tile"><svg viewBox="0 0 20 20"><circle cx="10" cy="10" r="3"/><circle cx="10" cy="10" r="7" stroke-dasharray="3 2"/></svg></div>
        <p class="feature-label">Efficient Workflow</p>
        <p class="fine">Shared tools keep planners aligned from kickoff to delivery.</p>
      </div>
      <div class="feature">
        <div class="feature-tile"><svg viewBox="0 0 20 20"><path d="M3 4h10v7H7l-3 3v-3H3z"/><path d="M15 8h2v7h-1v3l-3-3H9v-2"/></svg></div>
        <p class="feature-label">Customer Service</p>
        <p class="fine">Planners and architects reach a person who knows their project.</p>
      </div>
      <div class="feature">
        <div class="feature-tile"><svg viewBox="0 0 20 20"><circle cx="5" cy="10" r="2"/><circle cx="15" cy="4" r="2"/><circle cx="15" cy="16" r="2"/><path d="M7 9l6-4M7 11l6 4"/></svg></div>
        <p class="feature-label">Featured Network</p>
        <p class="fine">A wide partner network supports each regional site study.</p>
      </div>
    </div>
    <span class="rule"></span>
    <div class="company">
      <div>
        <p class="company-label">COMPANY INFO</p>
        <p class="fine">1200 Fenwick Way, Suite 300<br>Meridian, CO 80000</p>
      </div>
      <div>
        <p class="fine"><br>Phone: 000 555 0142<br>Fax: 000 555 0143</p>
      </div>
      <div>
        <p class="fine"><br>Email: info@bramblecrest.example<br>www.bramblecrest.example</p>
      </div>
    </div>
  </section>

  <section class="panel team">
    <h2 class="panel-title">Our team for your needs</h2>
    <div class="photo" style="left:150px;top:24px;width:108px;height:86px" role="img" aria-label="Portrait photo of a consultant in a suit"><span class="photo-tag">1</span><span class="photo-strip"></span></div>
    <div class="photo" style="left:264px;top:24px;width:102px;height:86px" role="img" aria-label="Portrait photo of a smiling consultant"><span class="photo-tag">2</span><span class="photo-strip"></span></div>
    <div class="photo" style="left:24px;top:116px;width:120px;height:84px" role="img" aria-label="Portrait photo of a team member in an office"><span class="photo-tag">3</span><span class="photo-strip"></span></div>
    <div class="photo" style="left:150px;top:116px;width:108px;height:84px" role="img" aria-label="Portrait photo of a cheerful team member"><span class="photo-tag">4</span><span class="photo-strip"></span></div>
    <div class="photo" style="left:264px;top:116px;width:102px;height:84px" role="img" aria-label="Portrait photo of a team member in a suit"><span class="photo-tag">5</span><span class="photo-strip"></span></div>
    <p class="team-lead">More than result. Get a preview of the upcoming year. Get a closer look. Driven by your ideas we will reach more results – be a part of our success.</p>
    <div class="team-columns">
      <div>
        <p class="fine">Bramblecrest Partners is proud to be an elite sponsor of the Northfield Civic Design Union conference this year.</p>
        <p class="fine"><strong>Customized consulting for communities and community planners.</strong></p>
        <p class="fine">Details: http://www.ncdumeridian.example/yearly-summit</p>
      </div>
      <div>
        <p class="fine"><strong>Economic Development Master Planning</strong> uses our proprietary approach to align every resource with local opportunity.</p>
        <p class="fine">Each plan ends with a concise report and clear next steps.</p>
      </div>
      <div>
        <p class="fine"><strong>Uncommon Insights — Aligning Resources to Opportunity.</strong> We help towns measure risk and compare options.</p>
        <p class="fine">Meet us at the NCDU booth to learn more.</p>
      </div>
    </div>
    <span class="rule"></span>
  </section>

  <section class="panel resilience">
    <span class="accent-bar"></span>
    <h2 class="panel-title">Resilience Assessment and Planning</h2>
    <ul class="bullets">
      <li>Instilling the agility to capitalize on opportunities</li>
      <li>Not surviving, but thriving during change</li>
      <li>Building awareness on the fringe</li>
    </ul>
    <div class="resilience-copy">
      <p class="fine">Resilience work starts with an honest look at exposure to shocks and stresses across the region.</p>
      <p class="fine">We pair local knowledge with proven models to rank risks and set priorities communities can act on.</p>
      <p class="fine">The result is a plan that keeps services running and invites new investment.</p>
    </div>
    <span class="rule"></span>
    <div class="photo hero-photo" role="img" aria-label="Photo of a smiling businessman in front of a rising growth chart"></div>
    <p class="overlay">Success being defined not only in terms of economics, but also in environmental outcomes, quality of life, enhanced service delivery, health, education, social and community values, and a host of other factors. Involving extensive community outreach and facilitation of consensus among stakeholders with divergent views</p>
  </section>

</main>
</body>
</html>
```